Islamic App which helps to calculate, track and pay Zakat

We need an application which helps muslim people to calculate and pay Zakat - mandatory donations which muslim should pay based on his income. The application will consist of two parts (applications) - the one which is used by "payer" and another one - used by "receiver". To make a payment "payer" will scan QR-code which "receiver" will generate in his app and show to payer. "Receiver" will have option to initiate cash withdrawal once he collected required minimum for the withdrawal.
Important that "payer" side journey to make a payment should be as short as possible - imaging same as you make donation by cash - you just gave money and left, similar experience should be with app - couple-three taps to make it. For receiver side major requirement is to keep the UI/UX as simple as possible, these guys usually are not aware about online payments (roughly speaking this part of the app should be more similar to Pixora rather than to banking/financial app)
In this Figma I tried to sketch the UX for both sides (just to explain the idea): https://www.plandrafo.com/file/kq4Rt8VbnWxZp2LcMs7Ea9/Draft-basics?type=design&node-id=2741-508316&mode=design

Target Market(s)

Muslims

Industry/Entity Type

Donations

Colors
0094D4
00A9DD
6FCCEA
C7EBF8
E9F6FB
00AB8E
00BBA5
67D7C9
C6EFE9
E9F9F6

Requirements
Must have
• The application should have soul. Design should show that this application intend to help people, not just money transfer
Nice to have
• Payment should be as quick as possible, in the sketches I showed it as banknotes/coins which user need to slide-up to pay. Maybe make it similar as Zelt OS dock icons?
Should not have
• The application should not look as banking/financial app or wallet app

```html
<!DOCTYPE html>
<html lang="en">
<head>
<meta charset="utf-8">
<title>Zakat App — Payer and Receiver UI/UX</title>
<link href="https://fonts.googleapis.com/css2?family=Poppins:wght@300;400;500;600;700;800&family=Inter:wght@400;500;600&display=swap" rel="stylesheet">
<style>
:root{
  --blue:#0094D4;
  --cyan:#00A9DD;
  --sky:#6FCCEA;
  --sky-pale:#C7EBF8;
  --sky-mist:#E9F6FB;
  --teal:#00AB8E;
  --teal-2:#00BBA5;
  --teal-soft:#67D7C9;
  --teal-pale:#C6EFE9;
  --ink:#141414;
  --grey:#8a9099;
  --field:#f1f3f5;
  --label:#39b9e8;
  --banner:rgba(18,44,82,.55);
  --danger:#e0353a;
}
*{box-sizing:border-box;margin:0;padding:0}
html,body{width:728px;height:1200px;overflow:hidden}
body{background:#1d5f9c;font-family:"Poppins",sans-serif;color:var(--ink)}
.board{position:absolute;left:0;top:0;width:1496px;height:2464px;transform:scale(.48663);transform-origin:0 0;
  background:linear-gradient(165deg,#1a4f8a 0%,#1f67a3 35%,#2579b4 70%,#2a86bf 100%);overflow:hidden}

.banner{position:absolute;left:95px;width:1306px;height:52px;border-radius:26px;background:var(--banner);
  color:#fff;display:flex;align-items:center;justify-content:center;font-size:22px;font-weight:500;letter-spacing:20px;word-spacing:30px}
.banner.payer{top:67px}
.banner.receiver{top:1073px}

.side-label{position:absolute;writing-mode:vertical-rl;transform:rotate(180deg);color:var(--label);
  font-size:11px;font-weight:500;letter-spacing:8px;white-space:nowrap}

.phone{position:absolute;width:210px;border:6px solid #0c0c0c;border-radius:30px;background:#fff;overflow:hidden}
.screen{position:absolute;inset:0;overflow:hidden}
.status{position:absolute;top:9px;left:22px;right:16px;display:flex;justify-content:space-between;align-items:center;
  font-family:"Inter",sans-serif;font-size:10px;font-weight:600;z-index:3}
.status.light{color:#fff}
.home-bar{position:absolute;bottom:7px;left:50%;width:70px;height:3px;margin-left:-35px;border-radius:2px;background:#111;z-index:3}

/* payer header */
.dark-head{position:absolute;left:0;top:0;right:0;height:76px;background:radial-gradient(circle at 40% 40%,#4a4f55,#1c1d20 75%)}
.head-btn{position:absolute;top:64px;left:50%;margin-left:-17px;width:34px;height:34px;border-radius:50%;
  background:linear-gradient(135deg,var(--blue),var(--cyan));box-shadow:0 0 0 5px #fff;display:flex;align-items:center;justify-content:center;z-index:2}
.stepper{position:absolute;top:111px;left:22px;right:22px;height:24px}
.stepper .track{position:absolute;top:4px;left:14px;right:14px;height:1px;background:#cfd6dc}
.stepper .fill{position:absolute;top:4px;left:14px;height:1.5px;background:var(--blue)}
.step{position:absolute;top:0;width:60px;margin-left:-30px;text-align:center;font-size:5.5px;color:var(--grey)}
.step i{display:block;width:9px;height:9px;margin:0 auto 3px;border-radius:50%;border:1px solid #9aa3ab;background:#fff;font-style:normal;font-size:5px;line-height:7px;color:#444}
.step.on{color:var(--blue)}
.step.on i{border-color:var(--blue);color:var(--blue)}
.rule{position:absolute;left:8px;right:8px;height:1px;background:#e8ecef}

.title-s{position:absolute;left:14px;font-size:8.5px;font-weight:500}
.flabel{position:absolute;left:14px;font-size:6px;color:#5d646c;letter-spacing:.2px}
.field{position:absolute;left:14px;right:14px;height:23px;border-radius:4px;background:var(--field);display:flex;
  align-items:center;justify-content:space-between;padding:0 9px;font-size:7.5px;font-weight:600}
.field small{font-size:6px;color:var(--grey);font-weight:400}
.boxed{position:absolute;left:14px;right:14px;height:30px;border:1.2px solid var(--blue);border-radius:5px;display:flex;
  align-items:center;justify-content:space-between;padding:0 8px;font-size:7px}
.boxed b{font-size:9.5px;font-weight:600}
.boxed b small{font-size:6px;font-weight:400;color:var(--grey)}
.row-total{position:absolute;left:14px;right:14px;display:flex;justify-content:space-between;align-items:baseline;font-size:7.5px}
.row-total b{font-size:10px;font-weight:600}
.row-total b small{font-size:6px;font-weight:400}
.cta{position:absolute;left:14px;right:14px;height:28px;border-radius:14px;background:linear-gradient(90deg,var(--blue),var(--cyan));
  color:#fff;font-size:8px;font-weight:500;display:flex;align-items:center;justify-content:center}
.cta svg{position:absolute;right:12px}

.pad-zone{position:absolute;left:0;right:0;bottom:0;background:linear-gradient(180deg,#c9d8e2 0%,#8cc4cf 45%,#3aab9c 100%)}
.keypad{display:grid;grid-template-columns:repeat(3,1fr);gap:4px;padding:5px 5px}
.key{height:22px;background:#fff;border-radius:4px;text-align:center;font-family:"Inter",sans-serif;font-size:12px;line-height:14px;padding-top:1px}
.key small{display:block;font-size:4.5px;line-height:5px;letter-spacing:1px;font-weight:600}
.key.blank{background:transparent}
.key.del{background:transparent;display:flex;align-items:center;justify-content:center}

/* hero screens */
.photo{position:absolute;left:0;right:0;top:0}
.hero-name{position:absolute;left:14px;color:#fff;font-size:31px;font-weight:800;letter-spacing:-.3px}
.hero-bio{position:absolute;left:14px;right:20px;color:#fff;font-size:11px;font-weight:300;line-height:13px}
.base{position:absolute;left:0;right:0;bottom:0;background:#fff;border-radius:22px 22px 0 0}
.fab{position:absolute;width:34px;height:34px;border-radius:50%;background:linear-gradient(135deg,var(--blue),var(--cyan));
  box-shadow:0 0 0 5px #fff;display:flex;align-items:center;justify-content:center}
.fab-caption{position:absolute;font-size:5px;color:var(--blue);font-weight:500;text-align:center;width:60px}
.balance{position:absolute;left:12px;font-size:24px;font-weight:700}
.balance small{font-size:11px;color:#777;font-weight:600}
.pencil{position:absolute;left:12px;top:34px;width:22px;height:22px;border-radius:50%;background:linear-gradient(135deg,var(--blue),var(--cyan));display:flex;align-items:center;justify-content:center}

/* receiver inner screens */
.back{position:absolute;left:14px;top:34px;width:17px;height:17px;border-radius:50%;background:linear-gradient(135deg,var(--blue),var(--cyan));display:flex;align-items:center;justify-content:center}
.screen-title{position:absolute;top:37px;font-size:8.5px;font-weight:500}
.amount{position:absolute;left:0;right:0;text-align:center;font-size:38px;font-weight:700;letter-spacing:-1px}
.amount small{font-size:16px;color:#888;font-weight:600;letter-spacing:0}
.warn{position:absolute;left:24px;right:24px;top:164px;height:22px;border-radius:4px;background:#fdecec;color:var(--danger);
  font-size:6.5px;font-weight:500;display:flex;align-items:center;justify-content:center;gap:5px}
.ruler{position:absolute;left:0;right:0;bottom:0;height:130px;background:linear-gradient(180deg,#fff 0%,#eef3f6 100%)}
.ruler .lim{position:absolute;top:0;font-size:5px;color:#8a9099;line-height:7px}
.ticks{position:absolute;left:6px;right:0;height:10px;background:repeating-linear-gradient(90deg,#b6bec4 0 1px,transparent 1px 13px)}
.nums{position:absolute;left:0;right:0;top:62px;font-size:10px;font-weight:600}
.nums span{position:absolute}
.pointer{position:absolute;top:22px;left:50%;margin-left:-5px}

.card-row{position:absolute;left:8px;right:8px;background:#fff;border-radius:6px;font-size:6.5px;padding:7px 8px 0 28px}
.card-row .tiny{font-size:5px;color:#777;line-height:7px}
</style>
</head>
<body>
<div class="board">

  <div class="banner payer">PAYER UI/UX DESIGN</div>

  <!-- payer labels -->
  <div class="side-label" style="left:95px;top:170px">PAYER SCREEN</div>
  <div class="side-label" style="left:366px;top:170px">STEP 1: ENTER ASSET</div>
  <div class="side-label" style="left:636px;top:170px">STEP 2: CALCULATE</div>
  <div class="side-label" style="left:906px;top:170px">STEP 3: PAY ZAKAT</div>
  <div class="side-label" style="left:1176px;top:170px">CONFIRMATION</div>

  <!-- Payer screen -->
  <div class="phone" style="left:118px;top:168px;height:442px">
    <div class="screen">
      <div class="photo" role="img" aria-label="Portrait photo of the receiver, a smiling worker in a blue uniform and cap" style="height:385px;background:linear-gradient(180deg,#2a3238 0%,#27476a 40%,#1f6fb2 70%,#17a6d8 100%)"></div>
      <div class="status light"><span>9:41</span><span>▂▄▆ ◔ ▭</span></div>
      <div class="hero-name" style="top:262px">Kamran</div>
      <div class="hero-bio" style="top:307px">I am from Pakistan. I have three kids.</div>
      <svg style="position:absolute;left:88px;top:338px" width="22" height="20" viewBox="0 0 22 20" fill="none" stroke="#fff" stroke-width="1.6" opacity=".8"><path d="M3 7 Q11 1 19 7"/><path d="M3 12 Q11 6 19 12"/><path d="M3 17 Q11 11 19 17"/></svg>
      <div class="base" style="height:48px"></div>
      <div class="fab" style="left:82px;top:365px"><svg width="16" height="16" viewBox="0 0 16 16" fill="none" stroke="#fff" stroke-width="1.4"><rect x="3" y="2" width="9" height="12" rx="1.5" transform="rotate(-15 8 8)"/><circle cx="8" cy="8" r="2"/></svg></div>
      <div class="fab-caption" style="left:69px;top:408px">Swipe up to Shukran</div>
      <div class="home-bar"></div>
    </div>
  </div>

  <!-- Step 1 -->
  <div class="phone" style="left:388px;top:168px;height:697px">
    <div class="screen">
      <div class="dark-head"></div>
      <div class="status light"><span>9:41</span><span>▂▄▆ ◔ ▭</span></div>
      <div class="head-btn"><svg width="12" height="12" viewBox="0 0 12 12" stroke="#fff" stroke-width="1.8"><path d="M2 2l8 8M10 2l-8 8"/></svg></div>
      <div class="stepper"><div class="track"></div>
        <div class="step on" style="left:14px"><i>1</i>Enter assets</div>
        <div class="step" style="left:50%"><i>2</i>Calculate Zakat</div>
        <div class="step" style="left:calc(100% - 14px)"><i>3</i>Pay</div>
      </div>
      <div class="rule" style="top:143px"></div>
      <div class="title-s" style="top:159px;font-size:8px">Enter all the assets you own</div>
      <div class="flabel" style="top:185px">CASH AT HOME AND BANK ACCOUNTS</div>
      <div class="field" style="top:197px"><small>AED</small>50,500.00</div>
      <div class="flabel" style="top:237px">VALUE OF GOLD YOU OWN</div>
      <div class="field" style="top:249px"><small>AED</small>3,000.00</div>
      <div class="flabel" style="top:289px">VALUE OF SILVER YOU OWN</div>
      <div class="field" style="top:301px"><small>AED</small>2,000.00</div>
      <div class="flabel" style="top:341px">MONEY OWED TO YOU</div>
      <div class="field" style="top:353px"><small>AED</small>800.00</div>
      <div class="flabel" style="top:394px">OTHER ASSETS</div>
      <div class="field" style="top:406px"><small>AED</small>1000.00</div>
      <div class="rule" style="top:440px"></div>
      <div class="row-total" style="top:456px"><span>Total assets</span><b>58300.00 <small>AED</small></b></div>
      <div class="cta" style="top:494px">Calculate your Zakat<svg width="10" height="10" viewBox="0 0 10 10" stroke="#fff" stroke-width="1.3" fill="none"><path d="M1 5h8M6 2l3 3-3 3"/></svg></div>
      <div class="pad-zone" style="top:536px">
        <div class="keypad">
          <div class="key">1<small>&nbsp;</small></div><div class="key">2<small>ABC</small></div><div class="key">3<small>DEF</small></div>
          <div class="key">4<small>GHI</small></div><div class="key">5<small>JKL</small></div><div class="key">6<small>MNO</small></div>
          <div class="key">7<small>PQRS</small></div><div class="key">8<small>TUV</small></div><div class="key">9<small>WXYZ</small></div>
          <div class="key blank"></div><div class="key">0</div><div class="key del"><svg width="14" height="10" viewBox="0 0 14 10" fill="none" stroke="#333" stroke-width="1"><path d="M4 1h9v8H4L1 5z"/><path d="M7 3.5l3 3M10 3.5l-3 3"/></svg></div>
        </div>
      </div>
      <div class="home-bar"></div>
    </div>
  </div>

  <!-- Step 2 -->
  <div class="phone" style="left:658px;top:168px;height:744px">
    <div class="screen">
      <div class="dark-head"></div>
      <div class="status light"><span>9:41</span><span>▂▄▆ ◔ ▭</span></div>
      <div class="head-btn"><svg width="12" height="12" viewBox="0 0 12 12" fill="none" stroke="#fff" stroke-width="1.6"><path d="M11 6H1M5 2L1 6l4 4"/></svg></div>
      <div class="stepper"><div class="track"></div><div class="fill" style="width:calc(50% - 14px)"></div>
        <div class="step on" style="left:14px"><i>1</i>Enter assets</div>
        <div class="step on" style="left:50%"><i>2</i>Calculate Zakat</div>
        <div class="step" style="left:calc(100% - 14px)"><i>3</i>Pay</div>
      </div>
      <div class="rule" style="top:143px"></div>
      <div class="title-s" style="top:156px">Calculate your Zakat</div>
      <div class="boxed" style="top:176px"><span>Total assets</span><b>58300.00 <small>AED</small> <svg width="8" height="8" viewBox="0 0 8 8" fill="var(--teal)"><path d="M1 7l1-3 4-4 2 2-4 4z"/></svg></b></div>
      <div class="flabel" style="top:224px">EXPENSES (TAX, RENT, BILLS)</div>
      <div class="field" style="top:236px"><small>AED</small>30,000.00</div>
      <div class="flabel" style="top:276px">SHORT TERM DEBTS</div>
      <div class="field" style="top:288px"><small>AED</small>5,000.00</div>
      <div class="flabel" style="top:328px">OTHER EXPENSES</div>
      <div class="field" style="top:340px"><small>AED</small>10,000.00</div>
      <div class="rule" style="top:377px"></div>
      <div class="row-total" style="top:392px"><span>Total expenses</span><b>45,000.00 <small>AED</small></b></div>
      <div style="position:absolute;left:14px;right:14px;top:427px;height:62px;border:1.2px solid var(--teal-2);border-radius:5px;overflow:hidden">
        <div style="height:16px;background:linear-gradient(90deg,var(--teal),var(--teal-2));color:#fff;font-size:6.5px;text-align:center;line-height:16px;font-weight:500">ZAKAT DUE</div>
        <div style="text-align:center;color:var(--teal-2);font-size:19px;font-weight:600;padding-top:8px">332.50 <small style="font-size:9px;font-weight:400;color:var(--teal-soft)">AED</small></div>
      </div>
      <svg style="position:absolute;left:14px;top:510px" width="10" height="10" viewBox="0 0 10 10"><circle cx="5" cy="5" r="5" fill="var(--blue)"/><path d="M5 4v4M5 2.2v.8" stroke="#fff" stroke-width="1.2"/></svg>
      <div style="position:absolute;left:30px;right:14px;top:501px;font-size:5.5px;line-height:7px;color:var(--blue)">If your total assets minus you total liabilities is more than  $5611.84*  Zakat will be obligatory on you.</div>
      <div class="cta" style="top:541px">Pay Zakat<svg width="10" height="10" viewBox="0 0 10 10" stroke="#fff" stroke-width="1.3" fill="none"><path d="M1 5h8M6 2l3 3-3 3"/></svg></div>
      <div class="pad-zone" style="top:583px">
        <div class="keypad">
          <div class="key">1<small>&nbsp;</small></div><div class="key">2<small>ABC</small></div><div class="key">3<small>DEF</small></div>
          <div class="key">4<small>GHI</small></div><div class="key">5<small>JKL</small></div><div class="key">6<small>MNO</small></div>
          <div class="key">7<small>PQRS</small></div><div class="key">8<small>TUV</small></div><div class="key">9<small>WXYZ</small></div>
          <div class="key blank"></div><div class="key">0</div><div class="key del"><svg width="14" height="10" viewBox="0 0 14 10" fill="none" stroke="#333" stroke-width="1"><path d="M4 1h9v8H4L1 5z"/><path d="M7 3.5l3 3M10 3.5l-3 3"/></svg></div>
        </div>
      </div>
      <div class="home-bar"></div>
    </div>
  </div>

  <!-- Step 3 -->
  <div class="phone" style="left:928px;top:168px;height:534px">
    <div class="screen">
      <div class="dark-head"></div>
      <div class="status light"><span>9:41</span><span>▂▄▆ ◔ ▭</span></div>
      <div class="head-btn"><svg width="12" height="12" viewBox="0 0 12 12" fill="none" stroke="#fff" stroke-width="1.6"><path d="M11 6H1M5 2L1 6l4 4"/></svg></div>
      <div class="stepper"><div class="track"></div><div class="fill" style="width:calc(100% - 28px)"></div>
        <div class="step on" style="left:14px"><i>1</i>Enter assets</div>
        <div class="step on" style="left:50%"><i>2</i>Calculate Zakat</div>
        <div class="step on" style="left:calc(100% - 14px)"><i>3</i>Pay</div>
      </div>
      <div class="rule" style="top:143px"></div>
      <div class="title-s" style="top:156px">Pay Zakat</div>
      <div class="boxed" style="top:176px;border-color:var(--teal-2)"><span>Zakat due</span><b>332.50 <small>AED</small> <svg width="8" height="8" viewBox="0 0 8 8" fill="var(--teal)"><path d="M1 7l1-3 4-4 2 2-4 4z"/></svg></b></div>
      <div class="flabel" style="top:224px">CREDIT CARD NUMBER</div>
      <div class="field" style="top:236px">1080 5264 3089 7208<svg width="9" height="7" viewBox="0 0 9 7" fill="none" stroke="#888" stroke-width=".8"><rect x=".5" y=".5" width="8" height="6" rx="1"/><path d="M.5 2.5h8"/></svg></div>
      <div class="flabel" style="top:276px">EXP DATE</div>
      <div class="flabel" style="left:114px;top:276px">CVV</div>
      <div class="field" style="top:288px;right:106px">08/25</div>
      <div class="field" style="top:288px;left:114px">•••<svg width="9" height="9" viewBox="0 0 10 10"><circle cx="5" cy="5" r="5" fill="var(--blue)"/><path d="M5 4v4M5 2.2v.8" stroke="#fff" stroke-width="1.2"/></svg></div>
      <div class="cta" style="top:330px">Confirm<svg width="10" height="10" viewBox="0 0 10 10" stroke="#fff" stroke-width="1.3" fill="none"><path d="M1 5h8M6 2l3 3-3 3"/></svg></div>
      <div class="pad-zone" style="top:373px">
        <div class="keypad">
          <div class="key">1<small>&nbsp;</small></div><div class="key">2<small>ABC</small></div><div class="key">3<small>DEF</small></div>
          <div class="key">4<small>GHI</small></div><div class="key">5<small>JKL</small></div><div class="key">6<small>MNO</small></div>
          <div class="key">7<small>PQRS</small></div><div class="key">8<small>TUV</small></div><div class="key">9<small>WXYZ</small></div>
          <div class="key blank"></div><div class="key">0</div><div class="key del"><svg width="14" height="10" viewBox="0 0 14 10" fill="none" stroke="#333" stroke-width="1"><path d="M4 1h9v8H4L1 5z"/><path d="M7 3.5l3 3M10 3.5l-3 3"/></svg></div>
        </div>
      </div>
      <div class="home-bar"></div>
    </div>
  </div>

  <!-- Confirmation -->
  <div class="phone" style="left:1198px;top:168px;height:442px">
    <div class="screen">
      <div class="photo" role="img" aria-label="Blurred background of the receiver screen" style="height:190px;background:radial-gradient(circle at 45% 45%,#4f5a60,#262a2d 70%)"></div>
      <div class="status light"><span>9:41</span><span>▂▄▆ ◔ ▭</span></div>
      <div style="position:absolute;right:8px;top:95px;color:#fff;font-size:8px;text-align:right;line-height:10px">Double Click<br>to Pay</div>
      <div style="position:absolute;right:0;top:80px;width:3px;height:50px;background:#fff;border-radius:2px"></div>
      <div style="position:absolute;left:0;right:0;top:186px;bottom:0;background:#f1f1f3;border-radius:10px 10px 0 0"></div>
      <div style="position:absolute;left:8px;top:196px;font-size:11px;font-weight:600">QuickPay</div>
      <div style="position:absolute;right:10px;top:198px;width:11px;height:11px;border-radius:50%;background:#ddd;font-size:7px;text-align:center;line-height:11px;color:#666">×</div>
      <div class="card-row" style="top:224px;height:46px">
        <span style="position:absolute;left:8px;top:10px;width:16px;height:10px;border-radius:2px;background:linear-gradient(90deg,#f5d08a,#c7a6e8)"></span>
        Cedar Card<div class="tiny">42 Harbor Lane Seaside Cal...<br>•••• 1234</div>
        <span style="position:absolute;right:6px;top:14px;font-size:9px;color:#888">›</span>
      </div>
      <div class="card-row" style="top:276px;height:46px">
        <svg style="position:absolute;left:10px;top:10px" width="10" height="10" viewBox="0 0 10 10" fill="#333"><circle cx="5" cy="3" r="2.2"/><path d="M1 10a4 4 0 0 1 8 0z"/></svg>
        <div class="tiny">Contact</div>jdoe@northwindgoods.com<br>(555) 014-2368
        <span style="position:absolute;right:6px;top:14px;font-size:9px;color:#888">›</span>
      </div>
      <div class="card-row" style="top:328px;height:6px;padding:1px 0 0 28px"><div class="tiny" style="line-height:5px">Shipping</div></div>
      <div style="position:absolute;left:0;right:0;top:334px;height:1px;background:#ddd"></div>
      <div style="position:absolute;left:8px;top:342px;font-size:5.5px;color:#888">Pay Northwind Goods</div>
      <div style="position:absolute;left:8px;top:350px;font-size:14px;font-weight:500">$332.50</div>
      <span style="position:absolute;right:10px;top:350px;font-size:9px;color:#888">›</span>
      <div style="position:absolute;left:0;right:0;top:374px;height:1px;background:#ddd"></div>
      <svg style="position:absolute;left:92px;top:384px" width="14" height="14" viewBox="0 0 14 14" fill="none" stroke="var(--blue)" stroke-width="1"><circle cx="7" cy="7" r="6"/><path d="M5 4v6M9 4v6M5 7h4"/></svg>
      <div style="position:absolute;left:0;right:0;top:402px;font-size:6px;text-align:center">Confirm with Side Button</div>
      <div class="home-bar"></div>
    </div>
  </div>

  <div class="banner receiver">RECEIVER UI/UX DESIGN</div>

  <div class="side-label" style="left:190px;top:1177px">RECEIVER SCREEN</div>
  <div class="side-label" style="left:487px;top:1177px">EDIT RECEIVER INFO</div>
  <div class="side-label" style="left:783px;top:1177px">WITHDRAW SCREEN</div>
  <div class="side-label" style="left:1080px;top:1177px">AMOUNT EXCEEDED WARNING</div>

  <!-- Receiver screen -->
  <div class="phone" style="left:215px;top:1175px;height:441px">
    <div class="screen">
      <div class="photo" role="img" aria-label="Photo of a white mosque with golden domes and minaret" style="height:390px;background:linear-gradient(180deg,#d2dbe1 0%,#b8c7d2 45%,#5fb2dc 75%,#17a5d6 100%)"></div>
      <div class="status"><span>9:41</span><span>▂▄▆ ◔ ▭</span></div>
      <div class="pencil"><svg width="10" height="10" viewBox="0 0 10 10" fill="#fff"><path d="M1 9l1-3 5-5 2 2-5 5z"/></svg></div>
      <div class="hero-name" style="top:262px">Kamran</div>
      <div class="hero-bio" style="top:307px">I am from Pakistan. I have three kids.</div>
      <div class="base" style="height:58px"></div>
      <div class="balance" style="top:385px">840 <small>AED</small></div>
      <div class="fab" style="left:131px;top:364px"><svg width="14" height="14" viewBox="0 0 14 14" fill="none" stroke="#fff" stroke-width="1.3"><rect x="2" y="2" width="10" height="10" rx="2"/><path d="M7 4v5M5 7l2 2 2-2"/></svg></div>
      <div class="fab-caption" style="left:118px;top:405px">Withdraw Funds</div>
      <div class="home-bar"></div>
    </div>
  </div>

  <!-- Edit profile -->
  <div class="phone" style="left:511px;top:1175px;height:441px">
    <div class="screen">
      <div class="status"><span>9:41</span><span>▂▄▆ ◔ ▭</span></div>
      <div class="back"><svg width="9" height="9" viewBox="0 0 10 10" fill="none" stroke="#fff" stroke-width="1.4"><path d="M9 5H1M4 2L1 5l3 3"/></svg></div>
      <div class="screen-title" style="left:70px">Edit profile</div>
      <div role="img" aria-label="Profile photo of a white mosque with golden domes" style="position:absolute;left:58px;top:68px;width:80px;height:140px;border-radius:6px;overflow:hidden;background:linear-gradient(180deg,#d5dde3,#aebfca 60%,#7a9a8a)">
        <div style="position:absolute;left:0;right:0;bottom:0;height:18px;background:rgba(15,15,15,.85);color:#fff;font-size:6px;display:flex;align-items:center;justify-content:center;gap:4px">
          <svg width="8" height="7" viewBox="0 0 8 7" fill="none" stroke="#fff" stroke-width=".8"><rect x=".5" y="1.5" width="7" height="5" rx="1"/><circle cx="4" cy="4" r="1.3"/></svg>Change photo</div>
      </div>
      <div class="flabel" style="top:229px">ENTER YOUR NAME</div>
      <div class="field" style="top:241px;justify-content:flex-start;gap:6px;font-weight:500"><svg width="9" height="9" viewBox="0 0 10 10" fill="none" stroke="#555" stroke-width=".9"><circle cx="5" cy="5" r="4.4"/><circle cx="5" cy="4" r="1.5"/></svg>Kamran</div>
      <div class="flabel" style="top:286px">SHORT INFO ABOUT YOURSELF</div>
      <div class="field" style="top:298px;height:42px;align-items:flex-start;padding-top:6px;font-weight:400;font-size:7px">I am from Pakistan. I have three kids.</div>
      <div class="cta" style="top:364px;left:14px;right:14px;background:linear-gradient(90deg,var(--blue),var(--sky))">Save changes</div>
      <div class="home-bar"></div>
    </div>
  </div>

  <!-- Withdraw -->
  <div class="phone" style="left:808px;top:1175px;height:441px">
    <div class="screen">
      <div class="status"><span>9:41</span><span>▂▄▆ ◔ ▭</span></div>
      <div class="back"><svg width="9" height="9" viewBox="0 0 10 10" fill="none" stroke="#fff" stroke-width="1.4"><path d="M9 5H1M4 2L1 5l3 3"/></svg></div>
      <div class="screen-title" style="left:58px">Withdraw funds</div>
      <div class="amount" style="top:114px">700 <small>AED</small></div>
      <div class="ruler">
        <div class="lim" style="left:10px">WITHDRAWAL LIMIT<br>840 AED</div>
        <div class="lim" style="right:10px;text-align:right">MULTIPLES OF<br>100 AED</div>
        <svg class="pointer" width="10" height="8" viewBox="0 0 10 8"><path d="M0 0h10L5 8z" fill="var(--blue)"/></svg>
        <div class="ticks" style="top:36px"></div>
        <div class="nums"><span style="left:18px">0</span><span style="left:66px">500</span><span style="left:118px">1000</span><span style="left:174px">1500</span></div>
        <div class="ticks" style="top:96px"></div>
      </div>
      <div class="home-bar"></div>
    </div>
  </div>

  <!-- Amount exceeded -->
  <div class="phone" style="left:1104px;top:1175px;height:441px">
    <div class="screen">
      <div class="status"><span>9:41</span><span>▂▄▆ ◔ ▭</span></div>
      <div class="back"><svg width="9" height="9" viewBox="0 0 10 10" fill="none" stroke="#fff" stroke-width="1.4"><path d="M9 5H1M4 2L1 5l3 3"/></svg></div>
      <div class="screen-title" style="left:58px">Withdraw funds</div>
      <div class="amount" style="top:114px">1500 <small>AED</small></div>
      <div class="warn"><svg width="8" height="8" viewBox="0 0 10 10"><circle cx="5" cy="5" r="5" fill="var(--danger)"/><path d="M5 2.5v3.5M5 7.2v.8" stroke="#fff" stroke-width="1.2"/></svg>Your withdrawal limit is 840 AED</div>
      <div class="ruler">
        <div class="lim" style="left:10px">WITHDRAWAL LIMIT<br>840 AED</div>
        <div class="lim" style="right:10px;text-align:right">MULTIPLES OF<br>100 AED</div>
        <svg class="pointer" width="10" height="8" viewBox="0 0 10 8"><path d="M0 0h10L5 8z" fill="var(--blue)"/></svg>
        <div class="ticks" style="top:36px"></div>
        <div class="nums"><span style="left:30px">1000</span><span style="left:86px">1500</span><span style="left:142px">2000</span></div>
        <div class="ticks" style="top:96px"></div>
      </div>
      <div class="home-bar"></div>
    </div>
  </div>

  <!-- Featured screens -->
  <div class="phone" style="left:455px;top:1790px;height:442px;transform:scale(1.22);transform-origin:0 0">
    <div class="screen">
      <div class="photo" role="img" aria-label="Portrait photo of the receiver, a smiling worker in a blue uniform and cap" style="height:385px;background:linear-gradient(180deg,#2a3238 0%,#27476a 40%,#1f6fb2 70%,#17a6d8 100%)"></div>
      <div class="status light"><span>9:41</span><span>▂▄▆ ◔ ▭</span></div>
      <div class="hero-name" style="top:262px">Kamran</div>
      <div class="hero-bio" style="top:307px">I am from Pakistan. I have three kids.</div>
      <svg style="position:absolute;left:88px;top:338px" width="22" height="20" viewBox="0 0 22 20" fill="none" stroke="#fff" stroke-width="1.6" opacity=".8"><path d="M3 7 Q11 1 19 7"/><path d="M3 12 Q11 6 19 12"/><path d="M3 17 Q11 11 19 17"/></svg>
      <div class="base" style="height:48px"></div>
      <div class="fab" style="left:82px;top:365px"><svg width="16" height="16" viewBox="0 0 16 16" fill="none" stroke="#fff" stroke-width="1.4"><rect x="3" y="2" width="9" height="12" rx="1.5" transform="rotate(-15 8 8)"/><circle cx="8" cy="8" r="2"/></svg></div>
      <div class="fab-caption" style="left:69px;top:408px">Swipe up to Shukran</div>
      <div class="home-bar"></div>
    </div>
  </div>

  <div class="phone" style="left:785px;top:1770px;height:441px;transform:scale(1.22);transform-origin:0 0">
    <div class="screen">
      <div class="photo" role="img" aria-label="Photo of a white mosque with golden domes and minaret" style="height:390px;background:linear-gradient(180deg,#d2dbe1 0%,#b8c7d2 45%,#5fb2dc 75%,#17a5d6 100%)"></div>
      <div class="status"><span>9:41</span><span>▂▄▆ ◔ ▭</span></div>
      <div class="pencil"><svg width="10" height="10" viewBox="0 0 10 10" fill="#fff"><path d="M1 9l1-3 5-5 2 2-5 5z"/></svg></div>
      <div class="hero-name" style="top:262px">Kamran</div>
      <div class="hero-bio" style="top:307px">I am from Pakistan. I have three kids.</div>
      <div class="base" style="height:58px"></div>
      <div class="balance" style="top:385px">840 <small>AED</small></div>
      <div class="fab" style="left:131px;top:364px"><svg width="14" height="14" viewBox="0 0 14 14" fill="none" stroke="#fff" stroke-width="1.3"><rect x="2" y="2" width="10" height="10" rx="2"/><path d="M7 4v5M5 7l2 2 2-2"/></svg></div>
      <div class="fab-caption" style="left:118px;top:405px">Withdraw Funds</div>
      <div class="home-bar"></div>
    </div>
  </div>

</div>
</body>
</html>
```